Solar energy proposal for homeowners

I am providing households with solar energy proposals, and I need a high-quality brochure that is packaged cleverly to attract the homeowner's attention. Take a look at the one page solar brochure that I have included to get an idea of text and content.

Target Market(s)

Residential Homeowners

Industry/Entity Type

Solar

Requirements
Must have
• High quality document

```html
<!DOCTYPE html>
<html lang="en">
<head>
<meta charset="utf-8">
<title>Brightvale Energy – Solar for $0 Down</title>
<link href="https://fonts.googleapis.com/css2?family=Montserrat:wght@400;500;600;700;800;900&display=swap" rel="stylesheet">
<style>
  :root{
    --navy:#0b2447;
    --navy-deep:#0e2350;
    --headline-blue:#173a6b;
    --teal:#13808f;
    --cyan:#2fc3dd;
    --cyan-bright:#22b8d6;
    --lime:#b5e31c;
    --white:#ffffff;
    --ink:#1a1a1a;
    --hero-sky:#6f95c2;
    --hero-mid:#8ea6c4;
    --hero-deep:#3a4d78;
  }
  *{margin:0;padding:0;box-sizing:border-box;}
  html,body{width:731px;height:1200px;overflow:hidden;background:#ffffff;}
  body{font-family:"Montserrat",Arial,sans-serif;}
  .flyer{position:relative;width:731px;height:1200px;overflow:hidden;background:var(--white);}

  /* Header band */
  .brand-band{position:absolute;left:0;top:0;width:731px;height:146px;
    background:linear-gradient(180deg,var(--navy) 0%,#0f4f72 60%,var(--teal) 100%);
    display:flex;align-items:center;justify-content:center;gap:14px;}
  .brand-mark{width:34px;height:34px;background:var(--cyan);}
  .brand-name{font-size:44px;font-weight:500;color:var(--cyan);letter-spacing:1px;}

  /* Hero */
  .hero-photo{position:absolute;left:0;top:146px;width:731px;height:350px;
    background:linear-gradient(180deg,var(--hero-sky) 0%,var(--hero-mid) 50%,var(--hero-deep) 100%);}
  .headline{position:absolute;left:0;top:168px;width:731px;text-align:center;text-transform:uppercase;}
  .headline .lead{display:block;font-size:38px;font-weight:800;color:var(--headline-blue);line-height:48px;letter-spacing:.5px;}
  .headline .punch{display:block;font-size:50px;font-weight:900;color:var(--navy-deep);line-height:54px;}
  .hero-tagline{position:absolute;left:42px;top:378px;font-size:9px;font-weight:500;color:var(--white);text-transform:uppercase;}

  /* Intro */
  .section-title{font-size:22px;font-weight:700;color:var(--navy-deep);text-transform:uppercase;}
  .about{position:absolute;left:45px;top:532px;width:330px;}
  .about p{margin-top:10px;font-size:14px;line-height:24px;color:var(--ink);text-align:justify;}
  .benefits{position:absolute;left:408px;top:532px;width:300px;}
  .benefits ul{list-style:none;margin-top:10px;}
  .benefits li{display:flex;align-items:center;gap:10px;font-size:14.5px;line-height:26.5px;color:var(--ink);}
  .benefits li b{color:var(--navy-deep);font-weight:700;}
  .tick{width:14px;height:14px;flex:none;}

  /* Services */
  .services{position:absolute;left:0;top:783px;width:731px;height:308px;background:var(--lime);}
  .services-title{position:absolute;left:0;top:12px;width:731px;display:flex;align-items:center;gap:14px;}
  .services-title::before,.services-title::after{content:"";flex:1;height:2px;background:var(--white);}
  .services-title h2{font-size:23px;font-weight:700;color:var(--navy-deep);text-transform:uppercase;}
  .service{position:absolute;width:300px;padding-left:36px;}
  .service h3{font-size:15px;font-weight:700;color:var(--navy-deep);text-transform:uppercase;line-height:22px;}
  .service p{font-size:14.5px;line-height:21px;color:var(--white);font-weight:500;}
  .service-icon{position:absolute;left:0;top:2px;width:28px;height:28px;border-radius:50%;background:var(--cyan-bright);border:2px solid var(--navy);}
  .s-pricing{left:38px;top:60px;}
  .s-install{left:386px;top:60px;}
  .s-local{left:38px;top:180px;}
  .s-eco{left:386px;top:180px;}

  /* Contact */
  .contact{position:absolute;left:0;top:1091px;width:731px;height:109px;background:var(--navy);}
  .contact-ribbon{position:absolute;left:0;top:1078px;width:731px;height:50px;}
  .contact-title{position:absolute;left:0;top:1087px;width:731px;text-align:center;font-size:24px;line-height:30px;font-weight:700;color:var(--white);text-transform:uppercase;}
  .contact-line{position:absolute;left:0;top:1157px;width:731px;display:flex;justify-content:center;align-items:center;gap:12px;
    font-size:14px;font-weight:700;color:var(--cyan);text-transform:uppercase;}
  .contact-item{display:flex;align-items:center;gap:8px;}
  .contact-item svg{width:14px;height:14px;}
</style>
</head>
<body>
<main class="flyer">
  <header class="brand-band">
    <span class="brand-mark"></span>
    <span class="brand-name">brightvale energy</span>
  </header>

  <div class="hero-photo" role="img" aria-label="Photo of solar panels in a field under the sun and a blue sky"></div>
  <h1 class="headline"><span class="lead">Solar for $0 Down</span><span class="punch">No Liens. No Kidding</span></h1>
  <p class="hero-tagline">Power your future with Brightvale Energy</p>

  <section class="about">
    <h2 class="section-title">About Us</h2>
    <p>At Brightvale Energy. our mission is to make solar simple and accessible for everyone. No high-pressure sales-just the information you need to make a smart choice. with our solar rental program. you can lower your monthly energy costs and pay less than your current electricity bill.</p>
  </section>

  <section class="benefits">
    <h2 class="section-title">Why Choose Us?</h2>
    <ul>
      <li><svg class="tick" viewBox="0 0 14 14"><circle cx="7" cy="7" r="7" fill="#1a1a1a"/><path d="M3.8 7.2l2.2 2.1 4.2-4.4" stroke="#fff" stroke-width="1.8" fill="none"/></svg><span><b>No</b> financing</span></li>
      <li><svg class="tick" viewBox="0 0 14 14"><circle cx="7" cy="7" r="7" fill="#1a1a1a"/><path d="M3.8 7.2l2.2 2.1 4.2-4.4" stroke="#fff" stroke-width="1.8" fill="none"/></svg><span><b>No</b> liens</span></li>
      <li><svg class="tick" viewBox="0 0 14 14"><circle cx="7" cy="7" r="7" fill="#1a1a1a"/><path d="M3.8 7.2l2.2 2.1 4.2-4.4" stroke="#fff" stroke-width="1.8" fill="none"/></svg><span><b>No</b> down payment</span></li>
      <li><svg class="tick" viewBox="0 0 14 14"><circle cx="7" cy="7" r="7" fill="#1a1a1a"/><path d="M3.8 7.2l2.2 2.1 4.2-4.4" stroke="#fff" stroke-width="1.8" fill="none"/></svg><span><b>No</b> insurance costs</span></li>
      <li><svg class="tick" viewBox="0 0 14 14"><circle cx="7" cy="7" r="7" fill="#1a1a1a"/><path d="M3.8 7.2l2.2 2.1 4.2-4.4" stroke="#fff" stroke-width="1.8" fill="none"/></svg><span><b>No</b> long-term commitment</span></li>
      <li><svg class="tick" viewBox="0 0 14 14"><circle cx="7" cy="7" r="7" fill="#1a1a1a"/><path d="M3.8 7.2l2.2 2.1 4.2-4.4" stroke="#fff" stroke-width="1.8" fill="none"/></svg><span><b>No</b> maintenance costs</span></li>
    </ul>
  </section>

  <section class="services">
    <div class="services-title"><h2>Our Best Service</h2></div>
    <article class="service s-pricing"><span class="service-icon"></span><h3>Affordable &amp; Transparent</h3><p>simple pricing, no hidden fees and a fixed monthly rate lower than typical energy bills.</p></article>
    <article class="service s-install"><span class="service-icon"></span><h3>Expert Installation</h3><p>Certified professionals handle installation, maintenance, and repairs end to end.</p></article>
    <article class="service s-local"><span class="service-icon"></span><h3>Local Expertise</h3><p>Florida-based team that under-stands the needs of Orlando and Statewide homeowners.</p></article>
    <article class="service s-eco"><span class="service-icon"></span><h3>Eco-Friendly</h3><p>Clean, renewable solar energy that helps reduce your carbon footprint.</p></article>
  </section>

  <footer>
    <div class="contact"></div>
    <svg class="contact-ribbon" viewBox="0 0 731 50" preserveAspectRatio="none" aria-hidden="true">
      <defs><linearGradient id="ribbonFill" x1="0" y1="0" x2="0" y2="1"><stop offset="0" stop-color="#1a9fc4"/><stop offset="1" stop-color="#2fd0ea"/></linearGradient></defs>
      <path d="M70 6 Q110 6 125 22 Q140 46 180 46 L551 46 Q591 46 606 22 Q621 6 661 6 Z" fill="url(#ribbonFill)"/>
    </svg>
    <h2 class="contact-title">Contact Us</h2>
    <div class="contact-line">
      <span class="contact-item"><svg viewBox="0 0 14 14"><path d="M3 1.5l2.2 2.6-1.2 1.6c.9 1.8 2.4 3.3 4.2 4.2l1.6-1.2 2.6 2.2-1.4 2c-5.3-.4-9.5-4.6-9.9-9.9z" fill="#b5e31c"/></svg>(407)555-0142</span>
      <span class="contact-item"><svg viewBox="0 0 14 14"><rect x="1" y="3" width="12" height="8" fill="#b5e31c"/><path d="M1 3l6 4.5L13 3" stroke="#0b2447" stroke-width="1.2" fill="none"/></svg>123 Anywhere St. Any City</span>
      <span class="contact-item"><svg viewBox="0 0 14 14"><circle cx="7" cy="7" r="5.8" stroke="#b5e31c" stroke-width="1.3" fill="none"/><ellipse cx="7" cy="7" rx="2.5" ry="5.8" stroke="#b5e31c" stroke-width="1.1" fill="none"/><path d="M1.2 7h11.6" stroke="#b5e31c" stroke-width="1.1"/></svg>www.brightvaleenergy.com</span>
    </div>
  </footer>
</main>
</body>
</html>
```